I need a label design/logo for a Shea Body Butter that I making. The body butter is made using Unrefined Shea Butter from Uganda. I have different mixes for the body butter depending on the Essential Oil used, for example - sweet orange, lavender, rosemary. The species of Shea tree in Uganda (Vitellaria Nilotica) is different from the one in West Africa (Vitellaria Paradoxa). As such, I would like the logo/label to have some reference to the Shea nut tree as well as the River Nile. Colours should be "fresh and earthy". I will be using round containers and I would like to be able to place the logo/label on round templates that I can stick on the containers. The name of the brand is "Tesi Ruka" Shea Body Butter.

```html
<!DOCTYPE html>
<html lang="en">
<head>
<meta charset="utf-8">
<title>Tesi Ruka Shea Butter – Sweet Orange Label</title>
<link rel="stylesheet" href="https://fonts.googleapis.com/css2?family=Cinzel:wght@400;500&family=Questrial&family=Montserrat:wght@500;600&display=swap">
<style>
  :root {
    --paper: #ffffff;
    --rim: #3e2f2a;
    --accent-orange: #e35a14;
    --nut-deep: #3a241c;
    --nut-mid: #6b3a26;
    --nut-light: #8a4a2e;
    --emblem-light: #d9d9d9;
    --emblem-mid: #9c9894;
    --title-panel: #5b4842;
    --title-rule: #e9e2de;
    --title-text: #f4f1ef;
    --brand-silver: #d2d2d2;
    --ribbon-dark: #6a4416;
    --ribbon-mid: #b07a2c;
    --ribbon-light: #c79040;
    --ribbon-text: #e4520c;
  }
  html, body {
    margin: 0;
    padding: 0;
    width: 1200px;
    height: 1171px;
    overflow: hidden;
    background: var(--paper);
  }
  .label {
    display: block;
    width: 1200px;
    height: 1171px;
  }
  .brand-name {
    font-family: "Questrial", sans-serif;
    font-size: 68px;
    fill: var(--brand-silver);
    letter-spacing: 2px;
  }
  .product-title {
    font-family: "Cinzel", serif;
    font-weight: 500;
    fill: var(--title-text);
  }
  .product-title--shea { font-size: 118px; letter-spacing: 30px; }
  .product-title--butter { font-size: 128px; letter-spacing: 22px; }
  .scent-name {
    font-family: "Montserrat", sans-serif;
    font-weight: 600;
    font-size: 46px;
    fill: var(--ribbon-text);
    letter-spacing: 1px;
  }
</style>
</head>
<body>
<svg class="label" viewBox="0 0 1200 1171" xmlns="http://www.w3.org/2000/svg">
  <defs>
    <radialGradient id="nut-field" cx="45%" cy="40%" r="65%">
      <stop offset="0%" stop-color="var(--nut-light)"/>
      <stop offset="55%" stop-color="var(--nut-mid)"/>
      <stop offset="100%" stop-color="var(--nut-deep)"/>
    </radialGradient>
    <radialGradient id="emblem-glow" cx="50%" cy="45%" r="60%">
      <stop offset="0%" stop-color="var(--emblem-light)" stop-opacity="0.85"/>
      <stop offset="60%" stop-color="var(--emblem-mid)" stop-opacity="0.55"/>
      <stop offset="100%" stop-color="var(--emblem-mid)" stop-opacity="0"/>
    </radialGradient>
    <linearGradient id="ribbon-band" x1="0" y1="0" x2="0" y2="1">
      <stop offset="0%" stop-color="var(--ribbon-mid)"/>
      <stop offset="50%" stop-color="var(--ribbon-light)"/>
      <stop offset="100%" stop-color="var(--ribbon-dark)"/>
    </linearGradient>
    <linearGradient id="ribbon-tail" x1="0" y1="0" x2="0" y2="1">
      <stop offset="0%" stop-color="var(--ribbon-dark)"/>
      <stop offset="100%" stop-color="#8a5a20"/>
    </linearGradient>
  </defs>

  <circle class="label__rim" cx="602" cy="581" r="545" fill="var(--rim)"/>
  <circle class="label__accent-ring" cx="602" cy="581" r="516" fill="none" stroke="var(--accent-orange)" stroke-width="10"/>

  <circle class="label__backdrop" cx="602" cy="581" r="508" fill="url(#nut-field)"
          role="img" aria-label="Close-up photograph of shea nuts in their shells"/>

  <rect class="label__emblem" x="456" y="110" width="300" height="285" rx="40" fill="url(#emblem-glow)"
        role="img" aria-label="Silver illustration of a shea nut tree beside a winding river"/>

  <text class="brand-name" x="606" y="465" text-anchor="middle">TESI RUKA</text>

  <g class="title-panel">
    <rect x="236" y="506" width="748" height="263" fill="var(--title-panel)"/>
    <rect x="242" y="512" width="736" height="251" fill="none" stroke="var(--title-rule)" stroke-width="2"/>
    <text class="product-title product-title--shea" x="617" y="610" text-anchor="middle">SHEA</text>
    <text class="product-title product-title--butter" x="620" y="740" text-anchor="middle">BUTTER</text>
  </g>

  <g class="scent-ribbon">
    <polygon points="267,820 362,812 362,920 290,925 318,872" fill="url(#ribbon-tail)"/>
    <polygon points="943,820 848,812 848,920 920,925 892,872" fill="url(#ribbon-tail)"/>
    <rect x="347" y="793" width="516" height="105" fill="url(#ribbon-band)"/>
    <line x1="347" y1="803" x2="863" y2="803" stroke="var(--accent-orange)" stroke-width="3"/>
    <line x1="347" y1="888" x2="863" y2="888" stroke="var(--accent-orange)" stroke-width="3"/>
    <text class="scent-name" x="605" y="862" text-anchor="middle">SWEET ORANGE</text>
  </g>
</svg>
</body>
</html>
```